Northfield Energy Product Distribution Brochure

We are looking to have our current brochure for our customers completely redesigned...the idea is to present the relevant information in an attractive way . Our website is northfieldenergy-example.com where you can find more information about us. We have included a file with a rough idea of the page order and what each should include but feel free to adapt based on design. The example provided is only for context and doesnt have to be maintained. We will be using the brochure both digitally and in print form. As long as it reads easily and is eye catching, the design can be horizontal or vertical.Final deliverable should be indesign file.

"Our Brands" page: should be limited to one page (space being enough) where it has the header for each one (for example diesel generators) space for one or two lines of text and then the corresponding logos for each of the five categories
Updates

For those asking: the "our brands" page should be a single page layout where there is a header with the corresponding section and space for maybe one line of text followed by the two logos for that category. Each of the product pages should be similar in fashion to the one in the document attached: a photo of the product with some white space and space for the text to be included. We will be posting additional examples today

Target Market(s)

We want to present it to customers both digitally and in print so they can see our products

Industry/Entity Type

Power Generation

Font styles to use
Serif

Requirements
Must have
• Eye catching and able to present the information in a presentable fashion. Rest is up to you.
Nice to have
• Should incorporate the colors of our logo but can also add other depending on design

```html
<!DOCTYPE html>
<html lang="en">
<head>
<meta charset="utf-8">
<title>Northfield Energy Product Distribution Brochure</title>
<link href="https://fonts.googleapis.com/css2?family=Lato:wght@300;400;700;900&display=swap" rel="stylesheet">
<style>
  :root{
    --canvas:#e6e6e6;
    --charcoal:#3a3a3c;
    --ink:#111111;
    --yellow:#f7e11a;
    --gold:#f3c316;
    --orange:#eea51c;
    --white:#ffffff;
    --body:#555555;
    --pale:#c9c9c9;
  }
  *{box-sizing:border-box;margin:0;padding:0}
  html,body{width:1200px;height:1200px;overflow:hidden;background:var(--canvas);font-family:"Lato",Arial,sans-serif}
  .spread{position:absolute;left:57px;width:1079px;height:381px;overflow:hidden;background:var(--charcoal);box-shadow:0 2px 6px rgba(0,0,0,.35)}
  .spread--products{top:12px}
  .spread--switches{top:407px}
  .spread--contact{top:801px}
  .spread svg.art{position:absolute;left:0;top:0;width:1079px;height:381px}
  .title{position:absolute;font-size:29px;line-height:1;letter-spacing:-.5px;white-space:nowrap}
  .title strong{font-weight:900;color:var(--yellow)}
  .title span{font-weight:300;color:var(--white)}
  .subtitle{position:absolute;font-size:11.5px;font-weight:900;color:#1a1a1a;letter-spacing:-.2px;text-transform:uppercase;white-space:nowrap}
  .copy{position:absolute;width:322px;font-size:5.9px;line-height:7.7px;color:var(--body);text-align:justify}
  .copy p+p{margin-top:8px}
  .page-no{position:absolute;top:350px;width:18px;height:18px;background:var(--ink);color:#ccc;font-size:5px;display:flex;align-items:center;justify-content:center}
  .page-no--left{left:0}
  .page-no--right{right:0}
  .distributor-list{position:absolute;left:568px;top:276px;list-style:none;font-size:8.6px;font-weight:700;color:#333;line-height:11.5px}
  .distributor-list li::before{content:"";display:inline-block;width:4px;height:4px;border-radius:50%;background:#222;margin:0 17px 1px 0;vertical-align:middle}
  .contact-number{position:absolute;left:195px;top:164px;font-size:20px;font-weight:300;color:var(--gold)}
  .contact-block{position:absolute;left:195px;font-size:6.6px;color:var(--white);line-height:8.4px}
  .contact-block h4{font-size:6.6px;font-weight:900;color:var(--gold);text-transform:uppercase}
</style>
</head>
<body>

<!-- Spread: Alternator parts / Controllers -->
<section class="spread spread--products">
  <svg class="art" viewBox="0 0 1079 381">
    <defs>
      <linearGradient id="bandYellow" x1="0" x2="1">
        <stop offset="0" stop-color="#f2b418"/><stop offset=".15" stop-color="#f7e11a"/>
        <stop offset=".85" stop-color="#f7e11a"/><stop offset="1" stop-color="#f2b418"/>
      </linearGradient>
      <linearGradient id="techBlue" x1="0" y1="0" x2="1" y2="1">
        <stop offset="0" stop-color="#0e2438"/><stop offset=".5" stop-color="#2c5574"/><stop offset="1" stop-color="#202a34"/>
      </linearGradient>
      <linearGradient id="techBlueR" x1="0" x2="1">
        <stop offset="0" stop-color="#3a3a3c"/><stop offset=".45" stop-color="#22405a"/><stop offset="1" stop-color="#2a2d33"/>
      </linearGradient>
      <linearGradient id="blackBar" x1="0" x2="1">
        <stop offset="0" stop-color="#000" stop-opacity=".2"/><stop offset=".3" stop-color="#000" stop-opacity=".95"/>
        <stop offset=".8" stop-color="#000" stop-opacity=".95"/><stop offset="1" stop-color="#000" stop-opacity=".3"/>
      </linearGradient>
      <linearGradient id="gutter" x1="0" x2="1">
        <stop offset="0" stop-color="#000" stop-opacity="0"/><stop offset=".5" stop-color="#000" stop-opacity=".12"/><stop offset="1" stop-color="#000" stop-opacity="0"/>
      </linearGradient>
    </defs>
    <rect x="0" y="0" width="539" height="175" fill="url(#techBlue)" role="img" aria-label="Blue circuit-board technology backdrop"/>
    <rect x="539" y="0" width="540" height="175" fill="url(#techBlueR)" role="img" aria-label="Dark circuit-board backdrop with glowing blue traces"/>
    <rect x="0" y="168" width="1079" height="54" fill="url(#blackBar)"/>
    <rect x="0" y="220" width="1079" height="161" fill="url(#bandYellow)"/>
    <polygon points="0,260 0,381 60,381" fill="#f0a81c" opacity=".7"/>
    <polygon points="1079,260 1079,381 1020,381" fill="#f0a81c" opacity=".7"/>
    <polygon points="158,258 918,258 988,381 88,381" fill="var(--white)"/>
    <rect x="20" y="10" width="255" height="160" rx="10" fill="#2a3038" opacity=".85" role="img" aria-label="Alternator voltage regulator boards"/>
    <rect x="25" y="188" width="165" height="62" rx="6" fill="#6d6f73" opacity=".9" role="img" aria-label="Alternator rotor assembly"/>
    <rect x="765" y="33" width="290" height="150" rx="10" fill="#1c1f24" opacity=".85" role="img" aria-label="Generator controller panels with digital displays"/>
    <rect x="519" y="0" width="40" height="381" fill="url(#gutter)"/>
  </svg>
  <h2 class="title" style="left:208px;top:192px"><strong>ALTERNATOR</strong> <span>PARTS</span></h2>
  <p class="subtitle" style="left:208px;top:233px">Aligning solutions together</p>
  <h2 class="title" style="left:573px;top:192px"><strong>CONTROLLERS</strong></h2>
  <p class="subtitle" style="left:574px;top:233px">Industry leading generator control</p>
  <div class="copy" style="left:192px;top:278px">
    <p>Northfield Energy supplies tested components for every stage of power generation. Our team selects each part for durability, fit and long service life, so your equipment keeps running when it matters most. Orders ship quickly from our central warehouse, with expert support available to help you choose the right solution. We stock leading brands and provide documentation, warranty service and on-site guidance for installers and facility managers across the region.</p>
    <p>Contact our sales staff for pricing, availability and technical data. We work closely with contractors and distributors to deliver reliable equipment on schedule and within budget, backed by years of experience in the field.</p>
  </div>
  <div class="copy" style="left:567px;top:278px">
    <p>Northfield Energy supplies tested components for every stage of power generation. Our team selects each part for durability, fit and long service life, so your equipment keeps running when it matters most. Orders ship quickly from our central warehouse, with expert support available to help you choose the right solution. We stock leading brands and provide documentation, warranty service and on-site guidance for installers and facility managers across the region.</p>
    <p>Contact our sales staff for pricing, availability and technical data. We work closely with contractors and distributors to deliver reliable equipment on schedule and within budget, backed by years of experience in the field.</p>
  </div>
  <div class="page-no page-no--left">10</div>
  <div class="page-no page-no--right">11</div>
</section>

<!-- Spread: Transfer switches / Distributors -->
<section class="spread spread--switches">
  <svg class="art" viewBox="0 0 1079 381">
    <defs>
      <linearGradient id="bandYellow2" x1="0" x2="1">
        <stop offset="0" stop-color="#f2b418"/><stop offset=".15" stop-color="#f7e11a"/>
        <stop offset=".85" stop-color="#f7e11a"/><stop offset="1" stop-color="#f2b418"/>
      </linearGradient>
      <linearGradient id="techDark" x1="0" x2="1">
        <stop offset="0" stop-color="#1f3a50"/><stop offset=".6" stop-color="#343a42"/><stop offset="1" stop-color="#3a3a3c"/>
      </linearGradient>
      <radialGradient id="mapGlow" cx=".5" cy=".5" r=".6">
        <stop offset="0" stop-color="#7fb2cc"/><stop offset=".6" stop-color="#365f76"/><stop offset="1" stop-color="#3a3a3c"/>
      </radialGradient>
      <linearGradient id="blackBar2" x1="0" x2="1">
        <stop offset="0" stop-color="#000" stop-opacity=".1"/><stop offset=".35" stop-color="#000" stop-opacity=".9"/>
        <stop offset=".75" stop-color="#000" stop-opacity=".95"/><stop offset="1" stop-color="#000" stop-opacity=".3"/>
      </linearGradient>
      <linearGradient id="gutter2" x1="0" x2="1">
        <stop offset="0" stop-color="#000" stop-opacity="0"/><stop offset=".5" stop-color="#000" stop-opacity=".12"/><stop offset="1" stop-color="#000" stop-opacity="0"/>
      </linearGradient>
    </defs>
    <rect x="0" y="0" width="539" height="170" fill="url(#techDark)" role="img" aria-label="Dark blue circuit-board backdrop"/>
    <rect x="700" y="0" width="379" height="170" fill="url(#mapGlow)" role="img" aria-label="Glowing blue world map"/>
    <rect x="0" y="168" width="1079" height="54" fill="url(#blackBar2)"/>
    <rect x="0" y="220" width="1079" height="161" fill="url(#bandYellow2)"/>
    <polygon points="0,260 0,381 60,381" fill="#f0a81c" opacity=".7"/>
    <polygon points="1079,260 1079,381 1020,381" fill="#f0a81c" opacity=".7"/>
    <polygon points="158,258 918,258 988,381 88,381" fill="var(--white)"/>
    <rect x="25" y="22" width="345" height="155" fill="#b9bcbf" role="img" aria-label="Automatic transfer switch cabinets"/>
    <rect x="25" y="177" width="155" height="76" fill="#a9acaf" role="img" aria-label="Open transfer switch cabinet showing internal switchgear"/>
    <rect x="519" y="0" width="40" height="381" fill="url(#gutter2)"/>
  </svg>
  <h2 class="title" style="left:216px;top:192px"><strong>TRANSFER</strong> <span>SWITCHES</span></h2>
  <p class="subtitle" style="left:216px;top:233px">The key to safe and convenient operation</p>
  <h2 class="title" style="left:565px;top:192px"><span>OUR</span> <strong>DISTRIBUTORS</strong></h2>
  <div class="copy" style="left:192px;top:278px">
    <p>Northfield Energy supplies tested components for every stage of power generation. Our team selects each part for durability, fit and long service life, so your equipment keeps running when it matters most. Orders ship quickly from our central warehouse, with expert support available to help you choose the right solution. We stock leading brands and provide documentation, warranty service and on-site guidance for installers and facility managers across the region.</p>
    <p>Contact our sales staff for pricing, availability and technical data. We work closely with contractors and distributors to deliver reliable equipment on schedule and within budget, backed by years of experience in the field.</p>
  </div>
  <ul class="distributor-list">
    <li>LOREM IPSUM DOLOR SIT AMET</li>
    <li>CONSECTETUR ADIPISCING ELIT, SED DO</li>
    <li>SED DO EIUSMOD TEMPOR</li>
    <li>LOREM IPSUM DOLOR SIT AMET</li>
    <li>CONSECTETUR ADIPISCING ELIT, SED DO</li>
    <li>SED DO EIUSMOD TEMPOR</li>
    <li>LOREM IPSUM DOLOR SIT AMET</li>
  </ul>
  <div class="page-no page-no--left">12</div>
  <div class="page-no page-no--right">13</div>
</section>

<!-- Spread: Location / Notes -->
<section class="spread spread--contact">
  <svg class="art" viewBox="0 0 1079 381">
    <defs>
      <linearGradient id="bandYellow3" x1="0" x2="1">
        <stop offset="0" stop-color="#f5d90a"/><stop offset=".5" stop-color="#f4c21a"/><stop offset="1" stop-color="#f7ec2a"/>
      </linearGradient>
      <linearGradient id="blackBar3" x1="0" x2="1">
        <stop offset="0" stop-color="#000" stop-opacity=".1"/><stop offset=".2" stop-color="#000" stop-opacity=".95"/>
        <stop offset=".8" stop-color="#000" stop-opacity=".95"/><stop offset="1" stop-color="#000" stop-opacity=".2"/>
      </linearGradient>
      <linearGradient id="cityBlue" x1="0" y1="0" x2="0" y2="1">
        <stop offset="0" stop-color="#2a4a66"/><stop offset="1" stop-color="#0f1b28"/>
      </linearGradient>
      <linearGradient id="notesWhite" x1="0" x2="1">
        <stop offset="0" stop-color="#ffffff"/><stop offset="1" stop-color="#d6d6d6"/>
      </linearGradient>
      <linearGradient id="gutter3" x1="0" x2="1">
        <stop offset="0" stop-color="#000" stop-opacity="0"/><stop offset=".5" stop-color="#000" stop-opacity=".14"/><stop offset="1" stop-color="#000" stop-opacity="0"/>
      </linearGradient>
    </defs>
    <rect x="0" y="37" width="1079" height="54" fill="url(#blackBar3)"/>
    <rect x="0" y="91" width="1079" height="36" fill="url(#bandYellow3)"/>
    <rect x="0" y="127" width="1079" height="254" fill="var(--charcoal)"/>
    <polygon points="0,127 178,127 0,300" fill="var(--pale)"/>
    <rect x="340" y="127" width="400" height="254" fill="url(#cityBlue)" role="img" aria-label="Large map pin over a blue city skyline with data charts"/>
    <polygon points="718,127 1079,127 1079,381 573,381" fill="url(#notesWhite)"/>
    <g stroke="#b5b5b5" stroke-width=".8">
      <line x1="728" y1="157" x2="1043" y2="157"/><line x1="728" y1="168" x2="1043" y2="168"/>
      <line x1="728" y1="179" x2="1043" y2="179"/><line x1="728" y1="190" x2="1043" y2="190"/>
      <line x1="728" y1="201" x2="1043" y2="201"/><line x1="728" y1="212" x2="1043" y2="212"/>
      <line x1="728" y1="223" x2="1043" y2="223"/><line x1="728" y1="234" x2="1043" y2="234"/>
      <line x1="728" y1="245" x2="1043" y2="245"/><line x1="728" y1="256" x2="1043" y2="256"/>
      <line x1="728" y1="267" x2="1043" y2="267"/><line x1="728" y1="278" x2="1043" y2="278"/>
      <line x1="728" y1="289" x2="1043" y2="289"/><line x1="728" y1="300" x2="1043" y2="300"/>
      <line x1="728" y1="311" x2="1043" y2="311"/><line x1="728" y1="322" x2="1043" y2="322"/>
    </g>
    <g class="phone-icon">
      <circle cx="133" cy="214" r="50" fill="none" stroke="var(--gold)" stroke-width="9"/>
      <path d="M96 190 q-6 34 22 58 q22 18 44 14 l6-16 q-10-8-20-10 l-8 8 q-18-8-28-28 l8-8 q-2-10-10-20 z" fill="var(--gold)"/>
    </g>
    <rect x="519" y="0" width="40" height="381" fill="url(#gutter3)"/>
  </svg>
  <h2 class="title" style="left:195px;top:63px"><span>OUR</span> <strong>LOCATION</strong></h2>
  <h2 class="title" style="left:581px;top:63px"><span>NOTES</span></h2>
  <p class="contact-number">1-800-555-0142</p>
  <div class="contact-block" style="top:194px"><h4>Call us</h4><p>Toll Free: 1-800-555-0142</p></div>
  <div class="contact-block" style="top:220px"><h4>Fax us</h4><p>305-555-0198</p></div>
  <div class="contact-block" style="top:246px"><h4>Visit us</h4><p>Northfield Energy Limited, Inc.</p><p>1200 Harbor Point Avenue, Springfield, ST 00000, USA</p></div>
  <div class="page-no page-no--left">14</div>
  <div class="page-no page-no--right">15</div>
</section>

</body>
</html>
```